We need a home page that represents us as the best Veterinary Hospital in the State

We need webdesign for a Vet Hospital in Rio de Janeiro, Brazil.
We think the current design is very childish. We want something that looks more like a hospital and not a clinic.
We put a map to guide the content of the sections and also an example of a layout that we don't like but that may serve as a reference as a wireframe.

Target Market(s)

pet owners

Industry/Entity Type

Pet Care

Number of Pages Required

1 page

Requirements
Must have
• Here is a map of the sections and texts we think for home: https://qv.zx/4937018256?t=HpLrTnsKwe
Nice to have
• some sites we like:
https://www.valtoramed.br/Pages/Home.aspx
https://www.mediquiro.com/
Should not have
• This is a design that we started working on and the content is correct. But the layout is poor in detail, bad colors, CTA's without prominence.

https://orlenpixworks.plankview.app/console/share/KT7N2W8RXP/731905246

```html
<!DOCTYPE html>
<html lang="pt-BR">
<head>
<meta charset="utf-8">
<title>Vetara 24h</title>
<link href="https://fonts.googleapis.com/css2?family=Catamaran:wght@300;400;500;600;700&display=swap" rel="stylesheet">
<style>
:root{
  --blue:#1677c9;
  --blue-dark:#0f5fae;
  --red:#ee1b3f;
  --coral:#f0455a;
  --ink:#1c1c1c;
  --text:#444;
  --grey-bg:#f3f4f6;
  --card-bg:#f5f3f2;
  --white:#fff;
}
*{margin:0;padding:0;box-sizing:border-box}
html,body{width:1200px;height:3689px;overflow:hidden}
body{position:relative;font-family:"Catamaran",sans-serif;color:var(--ink);background:var(--white)}
.abs{position:absolute}
a{color:inherit;text-decoration:none}

/* header */
.header{top:0;left:0;width:1200px;height:109px;background:var(--white)}
.brand{left:143px;top:26px;display:flex;align-items:center;gap:12px;color:var(--blue);font-weight:700;font-size:42px;line-height:1}
.brand-mark{width:22px;height:22px;background:var(--red)}
.nav{right:145px;top:44px;display:flex;gap:14px;font-size:13px;font-weight:500;color:#222}

/* hero */
.hero{top:109px;left:0;width:1200px;height:478px;background:linear-gradient(90deg,#3f7fc4 0%,#7d7fb7 45%,#c9607c 75%,#dc5b75 100%)}
.hero-title{top:245px;left:0;width:1200px;text-align:center;color:var(--white);font-size:44px;font-weight:500;line-height:54px;text-shadow:0 2px 6px rgba(0,0,0,.25)}
.hero-sub{top:370px;left:0;width:1200px;text-align:center;color:var(--white);font-size:25px;font-weight:500;line-height:34px}

/* service tabs */
.tabs{top:544px;left:140px;width:915px;height:86px;background:var(--blue);border-radius:14px;display:flex;align-items:center}
.tab{display:flex;align-items:center;gap:12px;color:var(--white);font-size:15px;font-weight:600;height:100%;padding:0 14px}
.tab + .tab{border-left:1px solid rgba(255,255,255,.45)}
.tab svg{width:30px;height:30px}
.tab-active{top:538px;left:457px;width:243px;height:98px;background:var(--red);display:flex;align-items:center;justify-content:center;gap:10px;color:var(--white);font-size:15px;font-weight:600;box-shadow:0 6px 14px rgba(0,0,0,.2)}

/* section headings */
.section-title{left:0;width:1200px;text-align:center;font-size:44px;font-weight:500;line-height:1}
.section-title span{color:var(--blue)}

/* unit cards */
.unit{top:805px;width:294px;height:444px;background:var(--card-bg);box-shadow:0 3px 8px rgba(0,0,0,.12);text-align:center}
.unit-photo{height:245px;width:100%}
.unit-name{margin-top:22px;font-size:24px;font-weight:500}
.unit-desc{margin-top:12px;font-size:15px;color:var(--text);line-height:20px;padding:0 40px}
.unit-addr{margin-top:10px;font-size:15px;color:var(--text);line-height:20px;padding:0 6px}
.unit-btn{position:absolute;left:88px;bottom:-26px;width:118px;height:52px;border-radius:12px;color:var(--white);font-size:15px;font-weight:600;display:flex;align-items:center;justify-content:center;background:var(--blue)}
.unit-btn.coral{background:var(--coral)}

/* video band */
.video{top:1369px;left:0;width:1200px;height:516px;background:linear-gradient(120deg,#3e4a2a 0%,#5f5340 45%,#4a5531 75%,#36472a 100%)}
.video-title{top:1510px;left:0;width:1200px;text-align:center;color:var(--white);font-size:44px;font-weight:500;line-height:54px}
.play{top:1666px;left:502px}
.video-link{top:1684px;left:590px;color:var(--red);font-size:20px;text-decoration:underline}

/* testimonial */
.quote-card{top:2072px;left:255px;width:690px;height:248px;background:var(--white);border-radius:16px;box-shadow:0 4px 18px rgba(0,0,0,.1);text-align:center}
.quote-text{margin:0 auto;padding-top:75px;width:520px;font-size:15px;line-height:22.5px;color:var(--text)}
.stars{margin-top:12px;color:#f0a30a;font-size:16px;letter-spacing:2px}
.arrow-btn{width:32px;height:32px;border-radius:50%;display:flex;align-items:center;justify-content:center}
.avatar{top:2345px;left:574px;width:92px;height:92px;border-radius:50%;background:linear-gradient(135deg,#d9b89a,#8c6a52);box-shadow:0 4px 10px rgba(0,0,0,.2)}
.author{top:2370px;left:680px;font-size:14px;font-weight:500;line-height:21px;text-transform:uppercase}

/* blog */
.interest{top:2527px;left:0;width:1200px;height:643px;background:var(--grey-bg)}
.post{top:2716px;left:279px;width:775px;height:350px;background:var(--white);box-shadow:0 6px 16px rgba(22,119,201,.15)}
.post-photo{top:2754px;left:150px;width:287px;height:275px;background:linear-gradient(160deg,#f4f1ec,#e6ddd0);border:1px solid #ddd}
.post-title{top:2762px;left:473px;width:440px;font-size:35px;font-weight:300;line-height:38px;color:#222}
.post-date{top:2858px;left:473px;font-size:13px;color:var(--blue);display:flex;gap:8px;align-items:center}
.post-excerpt{top:2898px;left:473px;width:460px;font-size:13px;line-height:18px;color:#333}
.post-btn{top:2966px;left:473px;width:118px;height:34px;border:2px solid var(--red);color:var(--red);font-size:13px;font-weight:600;display:flex;align-items:center;justify-content:center}

/* footer */
.footer{top:3170px;left:0;width:1200px;height:413px;background:linear-gradient(135deg,#1a7fd4,#0f6fc4)}
.footer-tag{top:3232px;right:146px;color:var(--white);font-size:20px;font-weight:500}
.footer-brand{top:3306px;left:143px;display:flex;align-items:center;gap:14px;color:var(--white);font-weight:700;font-size:52px;line-height:1}
.footer-brand .brand-mark{background:var(--white);width:26px;height:26px}
.fcol{top:3282px;color:var(--white)}
.fcol h4{font-size:16px;font-weight:600;text-decoration:underline;margin-bottom:4px}
.fcol li{list-style:none;font-size:12.5px;line-height:21px}
.fdivider{top:3463px;left:146px;width:908px;height:1px;background:rgba(255,255,255,.45)}
.fvline{top:3478px;width:1px;height:90px;background:rgba(255,255,255,.45)}
.fbox-title{top:3474px;color:var(--white);font-size:21px;font-weight:500}
.fbox-text{top:3516px;color:var(--white);font-size:15px;font-weight:600}
.socials{top:3525px;left:177px;display:flex;gap:14px}
.socials span{width:32px;height:32px;border:2px solid var(--white);border-radius:50%}
.bottom{top:3583px;left:0;width:1200px;height:106px;background:var(--blue-dark);color:var(--white);text-align:center}
.bottom p:first-child{margin-top:32px;font-size:16px;font-weight:600}
.bottom p:last-child{margin-top:2px;font-size:12px}
</style>
</head>
<body>

<header class="abs header">
  <div class="abs brand"><span class="brand-mark"></span>Vetara 24h</div>
  <nav class="abs nav">
    <a>Units</a><a>Schedules</a><a>Specialties</a><a>Blog</a><a>Vaccines</a><a>Work With Us</a><a>The Vetara</a><a>Tutor Area</a><a>Team</a>
  </nav>
</header>

<section class="abs hero" role="img" aria-label="Foto de veterinária examinando um cão e um gato"></section>
<h1 class="abs hero-title">Dedicação 24h por dia 7 dias por<br>semana pra cuidar de quem você ama!</h1>
<p class="abs hero-sub">Excelentes médicos e infraestrutura completa por um<br>preço que cabe no seu bolso.</p>

<div class="abs tabs">
  <div class="tab" style="width:183px;padding-left:26px">
    <svg viewBox="0 0 30 30" fill="none" stroke="#fff" stroke-width="2"><circle cx="15" cy="9" r="5"/><path d="M6 27c0-6 4-10 9-10s9 4 9 10"/></svg>Pronto-Socorro
  </div>
  <div class="tab" style="width:134px">
    <svg viewBox="0 0 30 30" fill="none" stroke="#fff" stroke-width="2"><circle cx="15" cy="9" r="5"/><path d="M6 27c0-6 4-10 9-10s9 4 9 10M15 17v6"/></svg>Consultas
  </div>
  <div style="width:243px"></div>
  <div class="tab" style="width:126px;border-left:none">
    <svg viewBox="0 0 30 30" fill="none" stroke="#fff" stroke-width="2"><rect x="4" y="6" width="22" height="19" rx="2"/><circle cx="15" cy="16" r="5"/></svg>Vacinas
  </div>
  <div class="tab" style="width:229px">
    <svg viewBox="0 0 30 30" fill="none" stroke="#fff" stroke-width="2"><rect x="6" y="4" width="18" height="23" rx="2"/><path d="M10 12h10M10 17h10M10 22h6"/></svg>Resultado de Exames
  </div>
</div>
<div class="abs tab-active">
  <svg width="30" height="30" viewBox="0 0 30 30" fill="none" stroke="#fff" stroke-width="2"><rect x="4" y="6" width="16" height="20" rx="2"/><path d="M8 13h8M8 18h8M24 4v10a3 3 0 0 1-6 0"/></svg>Agendamento de Exames
</div>

<h2 class="abs section-title" style="top:726px">Unidades <span>Vetara</span></h2>

<article class="abs unit" style="left:145px">
  <div class="unit-photo" role="img" aria-label="Foto de veterinária examinando um cão" style="background:linear-gradient(135deg,#f1ece6,#c9a98a)"></div>
  <h3 class="unit-name">Taquara - RJ</h3>
  <p class="unit-desc">Pronto-Socorro, Atendimento Clínico e Especialidades</p>
  <p class="unit-addr">Rua das Palmeiras, 141, Taquara</p>
  <a class="unit-btn">Learn More</a>
</article>
<article class="abs unit" style="left:452px">
  <div class="unit-photo" role="img" aria-label="Foto de tosadora cuidando de um poodle" style="background:linear-gradient(135deg,#c8d6c0,#8d7a63)"></div>
  <h3 class="unit-name">Flamengo - RJ</h3>
  <p class="unit-desc">Pronto-Socorro, Atendimento Clínico e Especialidades</p>
  <p class="unit-addr">Rua Andaraí Alta, 230, Flamengo</p>
  <a class="unit-btn coral">Learn More</a>
</article>
<article class="abs unit" style="left:760px">
  <div class="unit-photo" role="img" aria-label="Foto de gato enrolado em toalha após o banho" style="background:linear-gradient(135deg,#7fb6da,#c9e4f3)"></div>
  <h3 class="unit-name">Copacabana - RJ</h3>
  <p class="unit-desc">Pronto-Socorro, Atendimento Clínico e Especialidades</p>
  <p class="unit-addr">Rua Coral Marinho, 194 - Copacabana, Rio de Janeiro - RJ, 22000-000</p>
  <a class="unit-btn">Learn More</a>
</article>

<section class="abs video" role="img" aria-label="Foto de cão e gato juntos na grama"></section>
<h2 class="abs video-title">Infraestrutura completa e equipe médica<br>disponível 24h todos os dias</h2>
<svg class="abs play" width="64" height="64" viewBox="0 0 64 64">
  <circle cx="32" cy="32" r="30" fill="none" stroke="#ee1b3f" stroke-width="3"/>
  <circle cx="32" cy="32" r="25" fill="#ee1b3f"/>
  <path d="M26 21l17 11-17 11z" fill="#1c1c1c"/>
</svg>
<a class="abs video-link">Veja o vídeo</a>

<h2 class="abs section-title" style="top:1968px">Que dizem alguns <span>Tutores</span></h2>
<div class="abs quote-card">
  <svg class="abs" style="left:325px;top:26px" width="40" height="34" viewBox="0 0 40 34" fill="#ee1b3f"><path d="M2 2h15v14c0 9-5 15-13 17l-2-4c5-2 7-5 7-9H2zM23 2h15v14c0 9-5 15-13 17l-2-4c5-2 7-5 7-9h-7z"/></svg>
  <p class="quote-text">Sed ut perspiciatis unde omnis iste natus error sit voluptatem accntium doloremque laudantium, totam rem aperiam, eaque ipsa quae ab illo intore veritatis et quasi architecto beatae vitae dicta sunt explicabo. Nemo enim ipsam voluptatem quia voluptas sit aspernatur aut odit aut fugit, sed quia consequuntur magni dolores eos qui ratione</p>
  <div class="stars">★★★★★</div>
</div>
<svg class="abs" style="left:830px;top:2315px" width="70" height="50" viewBox="0 0 70 50"><path d="M0 0h70L6 50z" fill="#fff"/></svg>
<div class="abs arrow-btn" style="left:239px;top:2176px;background:#e4e4e4"><svg width="12" height="12" viewBox="0 0 12 12"><path d="M8 1L3 6l5 5" stroke="#fff" stroke-width="2" fill="none"/></svg></div>
<div class="abs arrow-btn" style="left:929px;top:2176px;background:var(--red)"><svg width="12" height="12" viewBox="0 0 12 12"><path d="M4 1l5 5-5 5" stroke="#fff" stroke-width="2" fill="none"/></svg></div>
<div class="abs avatar" role="img" aria-label="Foto da tutora"></div>
<p class="abs author">Marlon T Vasque<br>Kentucky</p>

<section class="abs interest"></section>
<h2 class="abs section-title" style="top:2627px">Você pode se <span>Interessa por</span></h2>
<article class="abs post"></article>
<div class="abs post-photo" role="img" aria-label="Foto de filhote de labrador com estetoscópio"></div>
<h3 class="abs post-title">Nemo enim ipsam voluptat quia voluptas sit</h3>
<p class="abs post-date">
  <svg width="12" height="12" viewBox="0 0 12 12"><rect x="1" y="2" width="10" height="9" fill="#555"/><rect x="2" y="5" width="8" height="5" fill="#fff"/></svg>FEB 3, 2020 AT 9:42 AM
</p>
<p class="abs post-excerpt">Lorem ipsum dolor sit amet, cotur adipiscing elit, sed do eiusmod tempor incididunt ut labore et dolore magna aliqua.</p>
<a class="abs post-btn">LEIA MAIS</a>

<footer class="abs footer"></footer>
<p class="abs footer-tag">Complete and accessible quality veterinary medical care</p>
<div class="abs footer-brand"><span class="brand-mark"></span>Vetara 24h</div>
<div class="abs fcol" style="left:558px"><h4>Services</h4><ul><li>Emergency Room</li><li>Queries</li><li>Exams</li><li>Vaccines</li><li>Surgeries</li></ul></div>
<div class="abs fcol" style="left:687px"><h4>Vetara</h4><ul><li>Units</li><li>Blog</li><li>Work with us</li><li>Who we are</li></ul></div>
<div class="abs fcol" style="left:813px"><h4>Help</h4><ul><li>Ombudsman</li><li>Contact us</li></ul></div>
<div class="abs fcol" style="left:939px"><h4>Tutors</h4><ul><li>Tutor area</li><li>Schedules</li><li>Examination results</li></ul></div>
<div class="abs fdivider"></div>
<div class="abs fvline" style="left:480px"></div>
<div class="abs fvline" style="left:816px"></div>
<p class="abs fbox-title" style="left:146px">Follow us on social media</p>
<div class="abs socials"><span></span><span></span><span></span><span></span></div>
<p class="abs fbox-title" style="left:536px">Call center</p>
<p class="abs fbox-text" style="left:536px">Phone: +55 21 2000-4170</p>
<p class="abs fbox-title" style="left:921px">Whatsapp</p>
<p class="abs fbox-text" style="left:921px">+55 21 90000-3158</p>
<div class="abs bottom">
  <p>Responsável técnico : Dr. Caio Amaral - Médico Veterinário - CRMV-RJ 00000</p>
  <p>VETARA © 2021 All Rights Reserved.</p>
</div>

</body>
</html>
```